Brightwell Homes Guide Business card

I have had at the logo designed here and attached. The business compares off the plan apartments in Sydney and provides quick comparison for new home buyers e.g price, floor plans and location. I would like the complimentary colours used on the business card. I would like it be unique but also look professional. I also have a website to gain inspiration from www.brightwellhomesguide.com.au
Updates
Industry/Entity Type
Business
Contact Information for Business Card
Helen Vostrakis
Director of Business Development
e: helen.vostrakis@brightwellhomesguide.com.au
p: (02) 8143 7692
m: 0431 572 908
w: www.brightwellhomesguide.com.au
Look and feel
Each slider illustrates characteristics of the customer's brand and the style your logo design should communicate.

```html
<!DOCTYPE html>
<html lang="en">
<head>
<meta charset="utf-8">
<title>Brightwell Homes Guide – Business Card</title>
<link href="https://fonts.googleapis.com/css2?family=Open+Sans:wght@400;600;700&display=swap" rel="stylesheet">
<style>
  :root {
    --backdrop: #2b2b2b;
    --card: #050505;
    --white: #ffffff;
    --grey-text: #e6e6e6;
    --brand-green: #7ac143;
    --brand-blue: #1f8fd6;
    --divider: #3a3a3a;
  }
  * { margin: 0; padding: 0; box-sizing: border-box; }
  html, body {
    width: 1200px; height: 900px; overflow: hidden;
    background: var(--backdrop);
    font-family: "Open Sans", Arial, sans-serif;
  }
  .canvas { position: relative; width: 1200px; height: 900px; }

  .card {
    position: absolute;
    width: 560px; height: 320px;
    background: var(--card);
    border-radius: 22px;
    overflow: hidden;
  }

  /* Front */
  .card-front { left: 70px; top: 80px; }
  .front-brand {
    position: absolute; left: 0; right: 0; top: 112px;
    display: flex; align-items: center; justify-content: center; gap: 16px;
  }
  .front-brand .brand-mark {
    width: 46px; height: 46px; border: 6px solid var(--white);
  }
  .front-brand .brand-name {
    color: var(--white); font-weight: 700; font-size: 34px; line-height: 1.05;
  }
  .front-url {
    position: absolute; left: 0; right: 0; top: 232px;
    text-align: center; color: var(--grey-text);
    font-size: 14px; letter-spacing: 0.6px;
  }

  /* Back */
  .card-back { left: 570px; top: 500px; }
  .back-content {
    position: absolute; left: 0; right: 0; top: 96px;
    display: flex; align-items: flex-start; justify-content: center;
  }
  .contact-block { text-align: right; padding-right: 16px; }
  .contact-name {
    color: var(--white); font-weight: 700; font-size: 17px; letter-spacing: 1.5px;
  }
  .contact-role {
    color: var(--brand-blue); font-size: 11.5px; letter-spacing: 1px;
    margin-bottom: 12px;
  }
  .contact-line {
    display: flex; align-items: center; justify-content: flex-end; gap: 7px;
    color: var(--white); font-size: 12px; line-height: 19px; letter-spacing: 0.3px;
  }
  .contact-line svg { width: 9px; height: 9px; flex: none; }
  .divider { width: 1px; height: 64px; background: var(--divider); }
  .back-brand {
    display: flex; align-items: center; gap: 10px; padding-left: 16px; margin-top: 6px;
  }
  .back-brand .brand-mark {
    width: 34px; height: 34px; background: var(--brand-green);
  }
  .back-brand .brand-name {
    color: var(--brand-green); font-weight: 700; font-size: 22px; line-height: 1.05;
  }
  .edge-band {
    position: absolute; left: 0; right: 0; bottom: 0; height: 10px;
    background: linear-gradient(to right, var(--brand-green) 0 84%, var(--white) 84% 100%);
  }
</style>
</head>
<body>
<div class="canvas">

  <section class="card card-front" aria-label="Card front">
    <div class="front-brand">
      <span class="brand-mark"></span>
      <span class="brand-name">Brightwell<br>Homes Guide</span>
    </div>
    <p class="front-url">www.brightwellhomesguide.com.au</p>
  </section>

  <section class="card card-back" aria-label="Card back">
    <div class="back-content">
      <div class="contact-block">
        <p class="contact-name">HELEN VOSTRAKIS</p>
        <p class="contact-role">DIRECTOR</p>
        <p class="contact-line">(02) 8143 7692
          <svg viewBox="0 0 10 10"><path d="M2 1l2 2-1 1.3c.6 1.3 1.4 2.1 2.7 2.7L7 6l2 2-1.3 1.5C4.5 9 1 5.5.5 2.3z" fill="var(--brand-blue)"/></svg>
        </p>
        <p class="contact-line">info@brightwellhomesguide.com.au
          <svg viewBox="0 0 10 10"><rect x="0.8" y="2" width="8.4" height="6" fill="none" stroke="var(--brand-blue)" stroke-width="1.2"/><path d="M1 2.4l4 3 4-3" fill="none" stroke="var(--brand-blue)" stroke-width="1.1"/></svg>
        </p>
        <p class="contact-line">www.brightwellhomesguide.com.au
          <svg viewBox="0 0 10 10"><circle cx="5" cy="5" r="4.2" fill="none" stroke="var(--brand-blue)" stroke-width="1.1"/><path d="M1 5h8M5 .8c2 2.5 2 5.9 0 8.4M5 .8c-2 2.5-2 5.9 0 8.4" fill="none" stroke="var(--brand-blue)" stroke-width="0.9"/></svg>
        </p>
      </div>
      <div class="divider"></div>
      <div class="back-brand">
        <span class="brand-mark"></span>
        <span class="brand-name">Brightwell<br>Homes Guide</span>
      </div>
    </div>
    <div class="edge-band"></div>
  </section>

</div>
</body>
</html>
```